Consulting company needs website design

We need a simple, static website design for our consulting company. We are looking for a general design of the look and feel of the website. Initially, it will have these pages:
- Home
- About us
- Services
- Contact us
We have our own logo which I have attached to the brief.

We are looking for a simple website, with white background and the use of gray (darker) as the main theme. Simple fonts. The website should be responsive so it an be easily red in mobile devices.

As part of the project, we will need to receive at least the following items:
- Individual files with sample text to support the pages outlined above
- Necessary CSS files

Our current website is here: http://www.marlowvane.co/

Here are some examples of other website we like to be used as guideline:
- http://www.tornaviamundo.com/
-

Target Market(s)

Individuals and companies looking to hire our company to provide consulting services.

Industry/Entity Type

It Company

Coding

Coded - Design and coding required

Number of Pages Required

4 page

Font styles to use
Sans Serif

Requirements
Must have
• Main page should have the ability to embed Chirply feed into it.
• We prefer the design to use gray tones.

```html
<!DOCTYPE html>
<html lang="en">
<head>
<meta charset="utf-8">
<title>Marlow Vane Group</title>
<link rel="stylesheet" href="https://fonts.googleapis.com/css2?family=Questrial&family=Lato:wght@400;700;900&display=swap">
<style>
:root{
  --ink:#333333;
  --dark:#2f2f2f;
  --band:#5e5e5e;
  --mid:#777777;
  --light:#e6e6e6;
  --line:#cfcfcf;
  --white:#ffffff;
  --accent:#1da1f2;
  --hero-a:#c9d6e3;
  --hero-b:#5f7a96;
}
*{box-sizing:border-box;margin:0;padding:0}
html,body{width:1200px;height:2253px;overflow:hidden;background:var(--white)}
body{position:relative;font-family:"Lato",Arial,sans-serif;color:var(--ink)}
.abs{position:absolute}
.display{font-family:"Questrial","Century Gothic",sans-serif}

.top-rule{left:0;top:0;width:1200px;height:6px;background:var(--dark)}
.brand{left:80px;top:24px;display:flex;align-items:center;gap:14px}
.brand-mark{width:78px;height:78px;border-radius:50%;border:2px solid #9a9a9a}
.brand-name{font-family:"Questrial",sans-serif;font-size:31px;line-height:32px;color:var(--ink)}
.phone{right:80px;top:18px;display:flex;align-items:center;gap:10px;font-family:"Questrial",sans-serif;font-size:24px;color:var(--ink)}
.phone-icon{width:36px;height:36px;border-radius:50%;background:var(--dark);display:flex;align-items:center;justify-content:center}
.nav{right:69px;top:70px;display:flex;gap:0}
.nav a{display:block;height:42px;line-height:40px;padding:0 21px;margin-left:24px;font-family:"Questrial",sans-serif;font-size:16px;color:var(--ink);text-decoration:none;border:1.5px solid transparent}
.nav a.current{border-color:var(--ink)}

.hero{left:0;top:123px;width:1200px;height:487px;background:linear-gradient(120deg,var(--hero-a) 0%,#a9bdd1 45%,var(--hero-b) 75%,#d8b8a4 100%)}
.hero-title{left:82px;top:228px;font-family:"Questrial",sans-serif;font-weight:400;font-size:39px;line-height:49px;color:#2c2c2c;text-shadow:0 0 1px #2c2c2c,0 2px 8px rgba(255,255,255,.7)}
.dots{left:561px;top:457px;display:flex;gap:13px}
.dots span{width:16px;height:16px;border-radius:50%;border:2px solid var(--white)}
.dots span.on{background:var(--white)}

.welcome{left:0;top:660px;width:1200px;text-align:center}
.welcome h2{font-family:"Questrial",sans-serif;font-weight:400;font-size:35px;color:var(--ink)}
.welcome h2 b{font-family:"Lato",sans-serif;font-weight:700}
.divider{width:604px;height:20px;margin:6px auto 0;position:relative}
.divider:before{content:"";position:absolute;left:0;right:0;top:9px;border-top:1px solid var(--line)}
.divider i{position:absolute;left:293px;top:1px;width:18px;height:18px;border-radius:50%;background:var(--white);border:1px solid var(--line)}
.welcome p{width:1030px;margin:16px auto 0;font-size:15px;line-height:25px;color:#444}
.btn{display:inline-flex;align-items:center;justify-content:space-between;height:34px;padding:0 4px 0 18px;border-radius:17px;background:var(--dark);color:var(--white);font-size:14px;box-shadow:2px 3px 0 #bdbdbd;gap:16px}
.btn i{width:26px;height:26px;border-radius:50%;background:var(--white);display:flex;align-items:center;justify-content:center}
.welcome .btn{margin-top:26px}

.service-band{left:0;top:1122px;width:1200px;height:241px;background:var(--band)}
.card{top:924px;width:328px}
.card-photo{width:328px;height:261px;border:5px solid var(--dark);box-shadow:0 8px 10px rgba(0,0,0,.35)}
.card-icon{position:absolute;left:114px;top:198px;width:100px;height:63px;border-radius:50px 50px 0 0;background:var(--dark);display:flex;justify-content:center;padding-top:14px}
.card h3{margin-top:18px;font-family:"Questrial",sans-serif;font-weight:400;font-size:28px;line-height:32px;text-align:center;color:var(--white);text-shadow:0 2px 3px rgba(0,0,0,.4)}
.card .btn{position:absolute;left:95px;top:357px;height:36px;border:2px solid var(--white);box-shadow:none}
.photo-deal{background:linear-gradient(135deg,#a8b8c8,#e5e8ec 55%,#7b8794)}
.photo-plan{background:linear-gradient(160deg,#30475f,#6e91b0 55%,#22354a)}
.photo-team{background:linear-gradient(135deg,#f2f2f2,#cfc9c2 55%,#8b7e74)}

.feed{left:80px;top:1405px;width:471px;height:383px;border:2px solid #9a9a9a;background:var(--white)}
.feed-head{height:61px;background:var(--dark);display:flex;align-items:center;justify-content:space-between;padding:0 18px;color:var(--white)}
.feed-head h3{font-family:"Questrial",sans-serif;font-weight:400;font-size:32px}
.feed-head h3 b{font-family:"Lato",sans-serif;font-weight:700}
.feed-list{position:relative;height:265px;padding:0 16px 0 8px}
.feed-list:after{content:"";position:absolute;right:4px;top:6px;width:4px;height:252px;background:#ececec;border-top:56px solid #555}
.tweet{position:relative;height:129px;border-bottom:1px solid #bfe3f6;padding:14px 0 0 80px;font-size:12.5px;line-height:18px;color:#333}
.tweet-dot{position:absolute;left:24px;top:28px;width:24px;height:24px;border-radius:50%;background:var(--accent)}
.tweet-meta{font-size:13px;margin-bottom:4px}
.tweet-meta b{margin-right:14px}
.tweet p{margin-left:0}
.tweet p span{display:block;margin-left:-80px;padding-left:0}
.tweet small{position:absolute;right:20px;bottom:14px;font-size:12px;color:#999}
.feed-input{margin:9px 6px 0;height:36px;border:1px solid #d7d7d7;background:#f1f1f1;padding:0 12px;line-height:34px;font-size:13px;color:#a8a8a8}

.split{left:599px;top:1408px;width:2px;height:378px;background:#9a9a9a}
.why{left:638px;top:1410px;width:480px}
.why h3{font-family:"Questrial",sans-serif;font-weight:400;font-size:34px;padding-bottom:14px;border-bottom:1px solid #e3e3e3}
.why h3 b{font-family:"Lato",sans-serif;font-weight:900}
.why-list{position:relative;margin-top:30px;padding-left:34px}
.why-list:before{content:"";position:absolute;left:60px;top:40px;height:190px;border-left:1px solid #c9c9c9}
.why-item{position:relative;display:flex;gap:20px;height:95px}
.why-icon{width:54px;height:54px;background:var(--white);display:flex;align-items:center;justify-content:center;position:relative}
.why-item h4{font-size:18px;font-weight:900;margin-top:0}
.why-item p{font-size:14px;line-height:21px;color:#444;margin-top:2px}

.footer-curve{left:0;top:1850px;width:1200px;height:100px}
.footer-badge{left:571px;top:1818px;width:58px;height:58px;border-radius:50%;background:var(--white);border:2px solid #d0d0d0}
.footer{left:0;top:1948px;width:1200px;height:257px;background:var(--dark);color:var(--white)}
.fcol{position:absolute;top:12px}
.fcol h4{font-family:"Questrial",sans-serif;font-weight:400;font-size:23px;padding-bottom:10px;border-bottom:1px solid #555;width:130px}
.fcol.wide h4{width:270px}
.fsep{position:absolute;top:30px;width:1px;height:190px;background:#444}
.links{list-style:none;margin-top:14px;font-size:14px;line-height:31px}
.links li:before{content:"• ";}
.contact{margin-top:14px;font-size:14px;line-height:20px}
.contact b{display:block;font-size:15px}
.contact .row{display:flex;align-items:center;gap:10px;margin-top:14px}
.form{margin-top:14px;width:267px}
.field{height:35px;background:var(--white);border-radius:2px;margin-bottom:7px;padding:0 10px;line-height:35px;font-size:12px;color:#888}
.submit{width:124px;height:35px;background:#c8c8c8;color:#444;text-align:center;line-height:35px;font-size:15px;font-weight:700;margin-top:2px}
.social{list-style:none;margin-top:14px}
.social li{display:flex;align-items:center;gap:12px;height:44px;font-size:12px;font-weight:700}
.social i{width:33px;height:33px;border-radius:50%;background:#e8e8e8}
.copyright{left:0;top:2205px;width:1200px;height:48px;background:#1b1b1b;color:#e8e8e8;text-align:center;line-height:48px;font-size:13px}
</style>
</head>
<body>

<div class="abs top-rule"></div>

<header>
  <div class="abs brand">
    <span class="brand-mark"></span>
    <span class="brand-name">Marlow Vane<br>Group</span>
  </div>
  <div class="abs phone">
    <span class="phone-icon"><svg width="18" height="18" viewBox="0 0 24 24"><path fill="#fff" d="M6.6 10.8a15 15 0 0 0 6.6 6.6l2.2-2.2c.3-.3.7-.4 1-.2 1.1.4 2.3.6 3.6.6.6 0 1 .4 1 1V20c0 .6-.4 1-1 1A17 17 0 0 1 3 4c0-.6.4-1 1-1h3.5c.6 0 1 .4 1 1 0 1.3.2 2.5.6 3.6.1.3 0 .7-.2 1z"/></svg></span>
    +100 555 0142
  </div>
  <nav class="abs nav">
    <a class="current" href="#">Home</a>
    <a href="#">About Us</a>
    <a href="#">Services</a>
    <a href="#">Contact Us</a>
  </nav>
</header>

<section class="abs hero" role="img" aria-label="Photo of a hand placing a blue jigsaw puzzle piece into a puzzle"></section>
<h1 class="abs hero-title">We Specialise In Helping<br>Our Clients Succeed</h1>
<div class="abs dots"><span class="on"></span><span></span><span></span></div>

<section class="abs welcome">
  <h2>Welcome To <b>Marlow Vane Group</b></h2>
  <div class="divider"><i></i></div>
  <p>Lorem ipsum dolor sit amet, consectetur adipiscing elit. Sed vitae magna tellus. Aenean ante nunc, semper nec cursus non, rutrum ac eros. Vestibulum mattis justo ac dui bibendum consequat a ac ipsum. Praesent a arcu venenatis, auctor velit eu, suscipit libero. Quisque convallis, leo ac pharetra sagittis, ipsum arcu auctor urna, sit amet cursus risus augue in eros.</p>
  <span class="btn">Read More <i><svg width="10" height="12" viewBox="0 0 10 12"><path d="M2 1l5 5-5 5" stroke="#2f2f2f" stroke-width="2" fill="none"/></svg></i></span>
</section>

<div class="abs service-band"></div>

<article class="abs card" style="left:80px">
  <div class="card-photo photo-deal" role="img" aria-label="Photo of two businesspeople shaking hands"></div>
  <div class="card-icon"><svg width="30" height="30" viewBox="0 0 30 30"><rect x="3" y="11" width="10" height="10" fill="#fff"/><rect x="15" y="11" width="10" height="10" fill="#fff"/><rect x="9" y="3" width="10" height="7" fill="#fff"/></svg></div>
  <h3>Mergers &amp;<br>Acquisitions</h3>
  <span class="btn">Read More <i><svg width="10" height="12" viewBox="0 0 10 12"><path d="M2 1l5 5-5 5" stroke="#2f2f2f" stroke-width="2" fill="none"/></svg></i></span>
</article>

<article class="abs card" style="left:435px">
  <div class="card-photo photo-plan" role="img" aria-label="Photo of a businessman facing a wall of sketched charts and ideas"></div>
  <div class="card-icon"><svg width="32" height="30" viewBox="0 0 32 30"><circle cx="11" cy="18" r="7" fill="none" stroke="#fff" stroke-width="4" stroke-dasharray="3 2"/><circle cx="23" cy="8" r="5" fill="none" stroke="#fff" stroke-width="3" stroke-dasharray="2.5 1.5"/></svg></div>
  <h3>Corporate Finance &amp;<br>Restructuring</h3>
  <span class="btn">Read More <i><svg width="10" height="12" viewBox="0 0 10 12"><path d="M2 1l5 5-5 5" stroke="#2f2f2f" stroke-width="2" fill="none"/></svg></i></span>
</article>

<article class="abs card" style="left:790px">
  <div class="card-photo photo-team" role="img" aria-label="Photo of two colleagues reviewing work together at a desk"></div>
  <div class="card-icon"><svg width="34" height="28" viewBox="0 0 34 28"><rect x="2" y="2" width="30" height="14" rx="2" fill="none" stroke="#fff" stroke-width="2"/><circle cx="11" cy="10" r="3.5" fill="#fff"/><circle cx="23" cy="10" r="3.5" fill="#fff"/><path d="M4 26c0-5 3-8 7-8s7 3 7 8zM16 26c0-5 3-8 7-8s7 3 7 8z" fill="#fff"/></svg></div>
  <h3>Strategic<br>Communications</h3>
  <span class="btn">Read More <i><svg width="10" height="12" viewBox="0 0 10 12"><path d="M2 1l5 5-5 5" stroke="#2f2f2f" stroke-width="2" fill="none"/></svg></i></span>
</article>

<aside class="abs feed">
  <div class="feed-head">
    <h3>Chirply <b>Feeds</b></h3>
    <span style="width:30px;height:30px;border-radius:50%;background:#fff;display:block"></span>
  </div>
  <div class="feed-list">
    <div class="tweet">
      <span class="tweet-dot"></span>
      <div class="tweet-meta"><b>Chirply Dev</b>19 July, 2016</div>
      <p>@sampleuser lorem ipsum dolor sit amet, consectetur<br>adipiscing elit. Sed vitae magna tellus. Aenean ante nunc, sem<span style="margin-left:-80px">per nec cursus non, rutrum ac eros mattis justo ac dui.</span></p>
      <small>View on Chirply</small>
    </div>
    <div class="tweet">
      <span class="tweet-dot"></span>
      <div class="tweet-meta"><b>Chirply Dev</b>19 July, 2016</div>
      <p>@sampleuser lorem ipsum dolor sit amet, consectetur<br>adipiscing elit. Sed vitae magna tellus. Aenean ante nunc, sem<span style="margin-left:-80px">per nec cursus non, rutrum ac eros mattis justo ac dui.</span></p>
      <small>View on Chirply</small>
    </div>
  </div>
  <div class="feed-input">Chirp to @marlowvanegroup</div>
</aside>

<div class="abs split"></div>

<section class="abs why">
  <h3>Why <b>Choose Us</b></h3>
  <div class="why-list">
    <div class="why-item">
      <div class="why-icon"><svg width="46" height="46" viewBox="0 0 46 46" fill="none" stroke="#333" stroke-width="1.6"><path d="M23 3l10 5v11l-10 5-10-5V8z"/><path d="M13 19l10 5v11l-10 5-10-5V24zM33 19l10 5v11l-10 5-10-5V24z"/></svg></div>
      <div><h4>Our Modular Approach</h4><p>Lorem ipsum dolor sit amet, consectetuer adipiscing elit,<br>sed diam nonummy nibh euismod.</p></div>
    </div>
    <div class="why-item">
      <div class="why-icon"><svg width="48" height="46" viewBox="0 0 48 46"><rect x="3" y="4" width="32" height="24" fill="#333"/><circle cx="15" cy="16" r="7" fill="#fff"/><path d="M15 16V9a7 7 0 0 1 7 7z" fill="#333"/><path d="M19 28v14M12 42l7-14 7 14" stroke="#333" stroke-width="2" fill="none"/><circle cx="41" cy="10" r="4" fill="#333"/><rect x="37" y="15" width="8" height="16" fill="#333"/></svg></div>
      <div><h4>‘Hands-on’ Strategy</h4><p>Lorem ipsum dolor sit amet, consectetuer adipiscing elit,<br>sed diam nonummy nibh euismod.</p></div>
    </div>
    <div class="why-item">
      <div class="why-icon"><svg width="48" height="48" viewBox="0 0 48 48" fill="none" stroke="#333" stroke-width="3"><path d="M38 12A20 20 0 1 1 30 6"/><path d="M32 17A12 12 0 1 1 27 14"/><circle cx="24" cy="24" r="4"/><path d="M24 24L6 42" stroke-width="4"/><path d="M4 36v8h8" fill="#333"/></svg></div>
      <div><h4>Facilitate Decision-Making</h4><p>Lorem ipsum dolor sit amet, consectetuer adipiscing elit,<br>sed diam nonummy nibh euismod.</p></div>
    </div>
  </div>
</section>

<svg class="abs footer-curve" viewBox="0 0 1200 100" preserveAspectRatio="none" aria-hidden="true"><path d="M0 100 Q600 -60 1200 100Z" fill="#2f2f2f"/></svg>
<div class="abs footer-badge"></div>

<footer class="abs footer">
  <div class="fcol" style="left:80px">
    <h4>Quick Links</h4>
    <ul class="links"><li>Home</li><li>About Us</li><li>Services</li><li>Contact Us</li></ul>
  </div>
  <div class="fsep" style="left:259px"></div>
  <div class="fcol wide" style="left:310px">
    <h4>Contact Details</h4>
    <div class="contact">
      <b>Marlow Vane Group</b>
      123, Ut wisi enim ad minim veniam,<br>Mor nostrni tation -123 456
      <div class="row"><svg width="13" height="13" viewBox="0 0 24 24"><path fill="#fff" d="M6.6 10.8a15 15 0 0 0 6.6 6.6l2.2-2.2c.3-.3.7-.4 1-.2 1.1.4 2.3.6 3.6.6.6 0 1 .4 1 1V20c0 .6-.4 1-1 1A17 17 0 0 1 3 4c0-.6.4-1 1-1h3.5c.6 0 1 .4 1 1 0 1.3.2 2.5.6 3.6.1.3 0 .7-.2 1z"/></svg>(100) 555 0142</div>
      <div class="row"><svg width="14" height="13" viewBox="0 0 14 13"><rect x="3" y="0" width="8" height="4" fill="#fff"/><rect x="0" y="4" width="14" height="6" fill="#fff"/><rect x="3" y="8" width="8" height="5" fill="#fff" stroke="#2f2f2f"/></svg>(100) 555 0142</div>
      <div class="row"><svg width="14" height="10" viewBox="0 0 14 10"><rect width="14" height="10" fill="#fff"/><path d="M0 0l7 6 7-6" stroke="#2f2f2f" fill="none"/></svg>Info@marlowvane.co</div>
    </div>
  </div>
  <div class="fsep" style="left:584px"></div>
  <div class="fcol wide" style="left:638px">
    <h4>Quick Inquiry</h4>
    <div class="form">
      <div class="field">Name</div>
      <div class="field">Email</div>
      <div class="field">Message</div>
      <div class="submit">Submit</div>
    </div>
  </div>
  <div class="fsep" style="left:951px"></div>
  <div class="fcol" style="left:1003px">
    <h4 style="width:110px">Follow Us</h4>
    <ul class="social">
      <li><i></i>FRIENDPAGE</li>
      <li><i></i>CHIRPLY</li>
      <li><i></i>LINKPRO</li>
      <li><i></i>GLOBEPLUS</li>
    </ul>
  </div>
</footer>

<div class="abs copyright">Copyright © 2016 <b>Marlow Vane Group</b>. All Rights Reserved.</div>

</body>
</html>
```